Health Supplement Series for 60 tablets of pure Tamrel Vine Kernel powder

We need a packaging design theme for a health supplement for international consumers. Our initial product is called 'Tamrel Vine Kernel'. It is for general health and is particularly effective for diabetic symptoms.
We would like to see designs that are clean and fresh.
It should give the impression of professional, premium pharmaceutical grade products.
Our company logo is attached below.

Target Market(s)

International

Industry/Entity Type

Health And Wellness

Font styles to use
Serif
Sans Serif

Requirements
Must have
• Bottle and box packaging required.
• 1st product is bottle of 60 tablets of 0.5gm each.
Should not have
• Seals and other "must buy" "guaranteed" etc

```html
<!DOCTYPE html>
<html lang="en">
<head>
<meta charset="utf-8">
<title>Tamrel Vine Kernel – Dietary Supplement Label</title>
<link href="https://fonts.googleapis.com/css2?family=Raleway:wght@400;500;600;700&family=Roboto+Condensed:wght@500&display=swap" rel="stylesheet">
<style>
  :root {
    --label-white: #fbfbfb;
    --brand-green: #4f8f1e;
    --deep-green: #1f5e12;
    --leaf-green: #5a9a1f;
    --capsule-green-light: #8fc06a;
    --capsule-green-dark: #2c6a1c;
    --panel-grey: #e4e4e4;
    --capsule-white: #f6f6f6;
    --text-grey: #6b6b6b;
  }
  html, body {
    margin: 0;
    padding: 0;
    overflow: hidden;
  }
  .label {
    position: relative;
    width: 1200px;
    height: 1200px;
    background: var(--label-white);
    overflow: hidden;
    font-family: "Raleway", sans-serif;
  }
  .seal-strip {
    position: absolute;
    left: 600px;
    top: 0;
    width: 64px;
    height: 300px;
    background: var(--leaf-green);
  }
  .seal-strip .tab {
    position: absolute;
    left: 14px;
    width: 36px;
    height: 36px;
    background: var(--label-white);
    opacity: 0.85;
  }
  .seal-strip .tab-one { top: 190px; }
  .seal-strip .tab-two { top: 244px; }

  .brand-name {
    position: absolute;
    left: 300px;
    top: 1000px;
    transform-origin: left top;
    transform: rotate(-90deg);
    color: var(--brand-green);
    font-weight: 500;
    white-space: nowrap;
  }
  .brand-name .primary {
    display: block;
    font-size: 168px;
    line-height: 150px;
    letter-spacing: 6px;
  }
  .brand-name .secondary {
    display: block;
    font-size: 54px;
    line-height: 62px;
    letter-spacing: 2px;
  }
  .net-weight {
    position: absolute;
    left: 302px;
    top: 1020px;
    font-size: 28px;
    color: var(--text-grey);
  }

  .capsule-panel {
    position: absolute;
    left: 585px;
    top: 410px;
    width: 300px;
    height: 660px;
    border-radius: 56px;
    background: var(--panel-grey);
  }
  .capsule {
    position: absolute;
    left: 605px;
    top: 430px;
    width: 260px;
    height: 620px;
    border-radius: 130px;
    overflow: hidden;
    background: var(--capsule-white);
    box-shadow: 0 4px 10px rgba(0,0,0,0.15);
  }
  .capsule .lower-half {
    position: absolute;
    left: 0;
    bottom: 0;
    width: 100%;
    height: 330px;
    background: linear-gradient(180deg, var(--capsule-green-light) 0%, var(--leaf-green) 35%, var(--capsule-green-dark) 100%);
  }
  .product-name {
    position: absolute;
    left: 0;
    top: 100px;
    width: 100%;
    margin: 0;
    text-align: center;
    font-size: 38px;
    line-height: 46px;
    font-weight: 600;
    color: var(--deep-green);
  }
  .product-type {
    position: absolute;
    left: 0;
    top: 212px;
    width: 100%;
    margin: 0;
    text-align: center;
    font-size: 24px;
    line-height: 30px;
    letter-spacing: 1px;
    color: var(--text-grey);
  }
  .source-note {
    position: absolute;
    left: 0;
    top: 340px;
    width: 100%;
    margin: 0;
    text-align: center;
    font-family: "Roboto Condensed", sans-serif;
    font-weight: 500;
    font-size: 34px;
    line-height: 42px;
    color: #ffffff;
  }
  .count {
    position: absolute;
    left: 0;
    top: 510px;
    width: 100%;
    margin: 0;
    text-align: center;
    font-size: 40px;
    font-weight: 700;
    color: #ffffff;
  }

  .side-bar {
    position: absolute;
    left: 960px;
    width: 90px;
    height: 50px;
    background: var(--leaf-green);
  }
  .side-bar-one { top: 590px; }
  .side-bar-two { top: 710px; }
  .side-bar-three { top: 1085px; }
</style>
</head>
<body>
<div class="label">
  <div class="seal-strip">
    <span class="tab tab-one"></span>
    <span class="tab tab-two"></span>
  </div>

  <div class="brand-name">
    <span class="primary">NOVERA</span>
    <span class="secondary">BIOSCIENCE LIMITED</span>
  </div>
  <div class="net-weight">0.5gm</div>

  <div class="capsule-panel"></div>
  <div class="capsule">
    <div class="lower-half"></div>
    <h1 class="product-name">Tamrel Vine<br>Kernel</h1>
    <p class="product-type">DIETARY<br>SUPPLEMENT</p>
    <p class="source-note">From Fruit<br>Flower and<br>Seed</p>
    <p class="count">60</p>
  </div>

  <div class="side-bar side-bar-one"></div>
  <div class="side-bar side-bar-two"></div>
  <div class="side-bar side-bar-three"></div>
</div>
</body>
</html>
```